Political Mail Out Quintero front and back

Front
Esteban (9th Grade) Quintero!

What's that famous saying?

Show me who your friends are and I'll tell you who you really are!
(show the two guys)

Arturo Benavides is charged with voter fraud by changing voter addresses from across the RGV so they could vote in Edinburg
Back
Did Esteban (9th Grade) Quintero commit voter fraud when he ran for office in 2016?
(insert blurred photo)

Here is a list of people from all over the RGV that voted in Edinburg in the 2016 race.
Here is a break down:

(highlight the number and where they were first registered to vote)

9 People voted in Edinburg who were registered in Donna.
13 People voted in Edinburg who were registered in San Juan
8 People voted in Edinburg who were registered in Pharr
31 People voted in Edinburg who were registered in McAllen
2 People voted in Edinburg who were registered in La Joya
6 People voted in Edinburg who were registered in Edcouch
2 People voted in Edinburg who were registered in Mercedes
2 People voted in Edinburg who were registered in Monte Alto
6 People voted in Edinburg who were registered in Weslaco
1 Person voted in Edinburg who were registered in Penitas
3 People voted in Edinburg who were registered in Alamo
5 People voted in Edinburg who were registered in Elsa
6 People voted in Edinburg who were registered in Mission
1 Person voted in Edinburg who were registered in Alton

Will Esteban (9th Grade) Quintero CHEAT in 2020?

Only time will tell.

Vote Esteban (9th Grade) Quintero OUT of office.

```html
<!DOCTYPE html>
<html lang="en">
<head>
<meta charset="utf-8">
<title>Quintero Mail Out – Front and Back</title>
<link rel="stylesheet" href="https://fonts.googleapis.com/css2?family=Montserrat:wght@700;800;900&family=Figtree:wght@400;600;800&display=swap">
<style>
  :root {
    --navy: #0f2350;
    --yellow: #fdb100;
    --orange: #f2651b;
    --box-orange: #f7931e;
    --white: #ffffff;
    --ink: #111827;
    --stage: #e9e9e9;
    --heavy: "Montserrat", Arial, sans-serif;
    --body: "Figtree", Arial, sans-serif;
  }
  * { box-sizing: border-box; margin: 0; padding: 0; }
  html, body { width: 864px; height: 1200px; overflow: hidden; background: var(--stage); }
  .canvas { position: relative; width: 864px; height: 1200px; }
  .card { position: absolute; left: 32px; width: 800px; height: 500px; overflow: hidden; background: var(--white); }
  .card--front { top: 90px; }
  .card--back { top: 610px; }
  .card svg.shapes { position: absolute; inset: 0; }
  .abs { position: absolute; }

  /* Front */
  .headline { left: 27px; top: 30px; font: 900 47px/50px var(--heavy); color: var(--navy); letter-spacing: -2px; text-transform: uppercase; }
  .saying-q { left: 32px; top: 278px; font: 900 29px/28px var(--heavy); color: var(--navy); letter-spacing: -0.5px; text-transform: uppercase; }
  .saying { left: 23px; top: 364px; font: 600 19px/24px var(--body); color: var(--white); }
  .charge { left: 0; width: 800px; top: 416px; text-align: center; font: 400 17.5px/25px var(--body); color: var(--ink); }
  .brand { left: 364px; top: 34px; color: var(--white); font-family: var(--body); font-weight: 800; }
  .brand__first { font-size: 30px; line-height: 32px; }
  .brand__last { font-size: 46px; line-height: 48px; letter-spacing: 1px; }

  /* Back */
  .question { left: 32px; top: 12px; width: 410px; font: 900 20.5px/22px var(--heavy); color: var(--orange); text-transform: uppercase; letter-spacing: -0.3px; }
  .intro { left: 22px; top: 128px; width: 370px; font: 400 14px/17px var(--body); color: var(--navy); }
  .intro strong { font-weight: 800; }
  .tally { left: 23px; top: 172px; display: grid; grid-template-columns: 189px 189px; column-gap: 0; row-gap: 4px; list-style: none; }
  .tally li { font: 400 11px/11.5px var(--body); color: var(--ink); height: 23.5px; }
  .tally b { font-weight: 800; }
  .cheat { left: 21px; top: 394px; font: 900 17.5px/17px var(--heavy); color: var(--navy); text-transform: uppercase; letter-spacing: -0.6px; }
  .tell { left: 21px; top: 444px; font: 900 22px/24px var(--heavy); color: var(--navy); text-transform: uppercase; letter-spacing: -0.8px; }
  .vote-box { left: 296px; top: 374px; width: 125px; height: 107px; background: var(--box-orange); padding: 14px 0 0 8px; font: 900 15px/16px var(--heavy); color: var(--navy); text-transform: uppercase; letter-spacing: -0.4px; }
</style>
</head>
<body>
<main class="canvas">

  <section class="card card--front" aria-label="Mail out front">
    <svg class="shapes" viewBox="0 0 800 500" width="800" height="500" aria-hidden="false">
      <rect x="0" y="0" width="800" height="397" fill="var(--navy)"/>
      <defs>
        <linearGradient id="friendsTone" x1="0" y1="0" x2="1" y2="1">
          <stop offset="0" stop-color="#c98f73"/>
          <stop offset="0.5" stop-color="#b8b3ad"/>
          <stop offset="1" stop-color="#6f6f72"/>
        </linearGradient>
      </defs>
      <polygon points="430,175 560,125 800,95 800,397 500,397" fill="url(#friendsTone)" role="img" aria-label="Photo of the two friends smiling side by side, one in a white shirt and one in a grey polo"/>
      <polygon points="0,0 236,0 518,358 0,358" fill="var(--yellow)"/>
      <polygon points="0,358 640,358 664,397 0,397" fill="var(--navy)"/>
    </svg>
    <h1 class="abs headline">Esteban<br>(9th<br>Grade)<br>Quintero!</h1>
    <h2 class="abs saying-q">What's that<br>famous saying?</h2>
    <p class="abs saying">Show me who your friends are and I'll tell you who you really are!</p>
    <div class="abs brand">
      <div class="brand__first">Esteban “Steve”</div>
      <div class="brand__last">QUINTERO</div>
    </div>
    <p class="abs charge">Arturo Benavides is charged with voter fraud by changing voter addresses from<br>across the RGV so they could vote in Edinburg</p>
  </section>

  <section class="card card--back" aria-label="Mail out back">
    <svg class="shapes" viewBox="0 0 800 500" width="800" height="500">
      <defs>
        <linearGradient id="rosterBlur" x1="0" y1="0" x2="1" y2="1">
          <stop offset="0" stop-color="#eceef2"/>
          <stop offset="0.6" stop-color="#e2e4ea"/>
          <stop offset="1" stop-color="#d6d8de"/>
        </linearGradient>
      </defs>
      <path d="M0,78 C120,100 300,104 432,92 L380,500 H0 Z" fill="url(#rosterBlur)" role="img" aria-label="Blurred photo of a printed voter roll"/>
      <path d="M0,0 H453 L395,500 H378 L432,92 C300,102 120,98 0,76 Z" fill="var(--navy)"/>
      <path d="M0,76 C60,84 120,89 190,91" fill="none" stroke="#ffe600" stroke-width="3"/>
    </svg>
    <h2 class="abs question">Did Esteban (9th Grade) Quintero commit voter fraud when he ran for office in 2016?</h2>
    <p class="abs intro">Here is a list of people from all over the RGV that voted in Edinburg in the 2016 race. <strong>Here is a break down:</strong></p>
    <ul class="abs tally">
      <li><b>9 People</b> voted in Edinburg who<br>were registered in <b>Donna.</b></li>
      <li><b>2 People</b> voted in Edinburg who<br>were registered in <b>Monte Alto</b></li>
      <li><b>13 People</b> voted in Edinburg who<br>were registered in <b>San Juan</b></li>
      <li><b>6 People</b> voted in Edinburg who<br>were registered in <b>Weslaco</b></li>
      <li><b>8 People</b> voted in Edinburg who<br>were registered in <b>Pharr</b></li>
      <li><b>1 Person</b> voted in Edinburg who<br>were registered in <b>Penitas</b></li>
      <li><b>31 People</b> voted in Edinburg who<br>were registered in <b>McAllen</b></li>
      <li><b>3 People</b> voted in Edinburg who<br>were registered in <b>Alamo</b></li>
      <li><b>2 People</b> voted in Edinburg who<br>were registered in <b>La Joya</b></li>
      <li><b>5 People</b> voted in Edinburg who<br>were registered in <b>Elsa</b></li>
      <li><b>6 People</b> voted in Edinburg who<br>were registered in <b>Edcouch</b></li>
      <li><b>6 People</b> voted in Edinburg who<br>were registered in <b>Mission</b></li>
      <li><b>2 People</b> voted in Edinburg who<br>were registered in <b>Mercedes</b></li>
      <li><b>1 Person</b> voted in Edinburg who<br>were registered in <b>Alton</b></li>
    </ul>
    <p class="abs cheat">Will Esteban (9th Grade)<br>Quintero cheat in 2020?</p>
    <p class="abs tell">Only time will tell.</p>
    <p class="abs vote-box">Vote Esteban (9th Grade) Quintero out of office.</p>
  </section>

</main>
</body>
</html>
```